Wellness, weight management medical practice

We have a logo but want help designing and finalizing the business card. Japanese name. Will eventually be a holistic, full-service weight management and wellness center. Will be a virtual only practice to start.

```html
<!DOCTYPE html>
<html lang="en">
<head>
<meta charset="utf-8">
<title>Harumori Wellness – Business Card</title>
<link href="https://fonts.googleapis.com/css2?family=Cinzel:wght@400;500&family=Cormorant+Garamond:wght@400;500&display=swap" rel="stylesheet">
<style>
  :root {
    --page: #f1f1f2;
    --card: #ffffff;
    --ink: #161616;
    --gold-dark: #98702a;
    --gold-mid: #c2a55a;
    --gold-light: #f3e7a6;
    --gold-text: #d9b45e;
    --shadow: rgba(0, 0, 0, 0.18);
  }
  * { margin: 0; padding: 0; box-sizing: border-box; }
  html, body {
    width: 1200px; height: 1200px; overflow: hidden;
    background: var(--page);
  }
  .canvas { position: relative; width: 1200px; height: 1200px; }

  .card {
    position: absolute; width: 667px; height: 392px;
    background: var(--card);
    box-shadow: 4px 5px 10px var(--shadow);
    overflow: hidden;
  }
  .card--front { left: 191px; top: 228px; }
  .card--back  { left: 479px; top: 633px; }

  .gold-band {
    position: absolute; left: 0; top: 0; width: 178px; height: 100%;
    background: linear-gradient(180deg, var(--gold-dark) 0%, var(--gold-mid) 22%, var(--gold-mid) 38%, var(--gold-light) 54%, var(--gold-mid) 70%, var(--gold-mid) 86%, var(--gold-dark) 100%);
  }
  .seal {
    position: absolute; left: 45px; top: 109px; width: 176px; height: 176px;
    border-radius: 50%; background: var(--card);
    border: 2px solid var(--gold-mid);
    display: flex; align-items: center; justify-content: center;
  }
  .seal__name, .mark__name {
    font-family: "Cormorant Garamond", serif; font-weight: 500;
    color: var(--gold-text); letter-spacing: 0.06em; white-space: nowrap;
  }
  .seal__name { font-size: 24px; }

  .identity {
    position: absolute; right: 55px; top: 68px; text-align: right;
    font-family: "Cinzel", serif; color: var(--ink);
  }
  .identity__name { font-size: 34px; font-weight: 400; letter-spacing: 0.09em; line-height: 1; }
  .identity__tagline {
    display: flex; align-items: center; gap: 5px; margin-top: 6px;
    font-size: 11.5px; letter-spacing: 0.02em;
  }
  .identity__tagline::before, .identity__tagline::after {
    content: ""; flex: 1; height: 1px; background: var(--ink);
  }
  .identity__sub { margin-top: 6px; font-size: 7.6px; letter-spacing: 0.12em; }

  .contacts {
    position: absolute; right: 22px; top: 180px; list-style: none;
    font-family: "Cinzel", serif; font-size: 15.5px; color: var(--ink);
  }
  .contacts__item {
    display: flex; align-items: center; justify-content: flex-end;
    gap: 18px; height: 38.5px; white-space: nowrap;
  }
  .contacts__icon { width: 15px; height: 15px; fill: var(--gold-text); flex: none; }

  .mark {
    position: absolute; left: 252px; top: 106px; width: 186px; height: 186px;
    border-radius: 50%; border: 2px solid var(--gold-text);
    display: flex; align-items: center; justify-content: center;
  }
  .mark__name { font-size: 30px; }

  .back-rule {
    position: absolute; left: 0; top: 366px; width: 100%; height: 3px;
    background: linear-gradient(90deg, var(--gold-dark), var(--gold-mid) 30%, var(--gold-light) 55%, var(--gold-mid) 80%, var(--gold-dark));
  }
</style>
</head>
<body>
<main class="canvas">
  <section class="card card--front" aria-label="Business card front">
    <div class="gold-band"></div>
    <div class="seal"><span class="seal__name">Harumori</span></div>

    <header class="identity">
      <h1 class="identity__name">HARUMORI</h1>
      <p class="identity__tagline">HOLISTIC, FULL-SERVICE</p>
      <p class="identity__sub">WEIGHT MANAGEMENT AND WELLNESS CENTER</p>
    </header>

    <ul class="contacts">
      <li class="contacts__item"><span>+070 5312 48207 - 070 5312</span>
        <svg class="contacts__icon" viewBox="0 0 24 24"><path d="M6.6 10.8a15.1 15.1 0 0 0 6.6 6.6l2.2-2.2a1 1 0 0 1 1-.25 11.4 11.4 0 0 0 3.6.57 1 1 0 0 1 1 1V20a1 1 0 0 1-1 1A17 17 0 0 1 3 4a1 1 0 0 1 1-1h3.5a1 1 0 0 1 1 1c0 1.25.2 2.45.57 3.57a1 1 0 0 1-.25 1z"/></svg></li>
      <li class="contacts__item"><span>YOURMAIL@MAILBOX.COM</span>
        <svg class="contacts__icon" viewBox="0 0 24 24"><path d="M2 5h20v14H2z M2 5l10 8 10-8" fill="var(--gold-text)" stroke="#fff" stroke-width="1.2"/></svg></li>
      <li class="contacts__item"><span>YOUR STREET ADDRESS HERE STREET</span>
        <svg class="contacts__icon" viewBox="0 0 24 24"><path d="M12 2a7 7 0 0 0-7 7c0 5.2 7 13 7 13s7-7.8 7-13a7 7 0 0 0-7-7zm0 9.5A2.5 2.5 0 1 1 12 6.5a2.5 2.5 0 0 1 0 5z"/></svg></li>
      <li class="contacts__item"><span>WWW.YOURSITEHERE.COM</span>
        <svg class="contacts__icon" viewBox="0 0 24 24"><g fill="none" stroke="var(--gold-text)" stroke-width="1.6"><circle cx="12" cy="12" r="9.5"/><ellipse cx="12" cy="12" rx="4" ry="9.5"/><path d="M2.5 12h19M4 7h16M4 17h16"/></g></svg></li>
    </ul>
  </section>

  <section class="card card--back" aria-label="Business card back">
    <div class="mark"><span class="mark__name">Harumori</span></div>
    <div class="back-rule"></div>
  </section>
</main>
</body>
</html>
```